Flyer for family counseling

For my family counseling I'm looking for a design for flyers. Important is not only the appearance of the flyer, but also the content design. All important contents can be found on my website: www.helga-brandtner.at The following items should NOT appear on the flyer: - constellation work - bereavement and palliative work My logo should definitely be on the flyer. Source files are available.

Target Market(s)

Families, individuals, children, couples in need of psychological support.

Colors

Designer to choose colors to be used in the design.

Requirements
Must have
• My logo - source files available Website and contact data Recognition value from website to flyer and vice versa
Should not have
• Mention of the constellation work and mourning and palliative work not desired.

```html
<!DOCTYPE html>
<html lang="de">
<head>
<meta charset="utf-8">
<title>Familienberatung Stadlau – Flyer</title>
<link href="https://fonts.googleapis.com/css2?family=Ubuntu:ital,wght@0,300;0,400;0,500;1,300;1,400&display=swap" rel="stylesheet">
<style>
  :root {
    --teal-dark: #17a398;
    --teal-light: #2fd6c9;
    --teal-text: #169c92;
    --logo-blue: #1f5fa8;
    --ink: #222;
    --white: #fff;
    --photo-a: #eee3d0;
    --photo-b: #e2d2b8;
    --photo-c: #d9c7aa;
  }
  * { box-sizing: border-box; margin: 0; padding: 0; }
  html, body { width: 904px; height: 1200px; overflow: hidden; background: var(--white); }
  body { font-family: "Ubuntu", sans-serif; color: var(--ink); position: relative; }
  .abs { position: absolute; }

  .brand { left: 40px; top: 30px; width: 250px; text-align: center; }
  .brand-mark { width: 70px; height: 70px; border-radius: 50%; background: var(--teal-dark); margin: 0 auto 12px; }
  .brand-name { font-size: 15px; font-weight: 500; letter-spacing: 1px; color: var(--logo-blue); }

  .sq { background: var(--teal-dark); }
  .sq.light { background: var(--teal-light); }
  .web-bar { left: 510px; top: 64px; width: 394px; height: 50px; background: var(--teal-light);
    color: var(--white); font-size: 27px; font-weight: 400; line-height: 50px; padding-left: 25px; }

  .hero { left: 0; top: 165px; width: 904px; height: 398px;
    background: linear-gradient(120deg, var(--photo-a) 0%, var(--photo-b) 55%, var(--photo-c) 100%); }
  .hero-title { left: 0; top: 465px; width: 370px; height: 70px; background: var(--teal-light);
    color: var(--white); font-size: 27px; line-height: 70px; padding-left: 20px; }

  .service-img { width: 189px; height: 126px; border-bottom-right-radius: 28px;
    background: linear-gradient(135deg, var(--photo-a), var(--photo-c)); }
  .service-text { width: 196px; }
  .service-text h2 { font-size: 19px; font-weight: 400; color: var(--teal-text); margin-bottom: 6px; }
  .service-text p { font-size: 10.2px; line-height: 14px; text-align: justify;
    hyphens: auto; -webkit-hyphens: auto; }

  .voices { left: 0; top: 929px; width: 904px; height: 202px; background: var(--teal-dark); }
  .voices h2 { position: absolute; left: 48px; top: 20px; font-size: 26px; font-weight: 300; color: var(--white); }
  .quote { background: var(--white); height: 118px; top: 61px; padding: 20px 14px 0 14px;
    font-size: 12.5px; line-height: 16px; font-style: italic; font-weight: 300; }
  .quote p { text-align: justify; hyphens: auto; -webkit-hyphens: auto; }
  .quote .who { position: absolute; right: 42px; bottom: 10px; font-style: normal; font-weight: 400; font-size: 13px; }
  .qmark { position: absolute; font-size: 64px; font-weight: 500; color: var(--teal-light); line-height: 1; }

  .footer { left: 0; top: 1131px; width: 904px; height: 69px; background: var(--teal-light);
    color: var(--white); font-size: 14px; font-weight: 500; text-align: center; line-height: 69px; }
</style>
</head>
<body>
  <div class="abs brand">
    <div class="brand-mark"></div>
    <div class="brand-name">HELGA BRANDTNER</div>
  </div>

  <div class="abs sq" style="left:415px;top:64px;width:35px;height:50px"></div>
  <div class="abs sq light" style="left:464px;top:64px;width:34px;height:50px"></div>
  <div class="abs web-bar">www.helga-brandtner.at</div>

  <div class="abs hero" role="img" aria-label="Foto: Beraterin im Gespräch mit einer Familie in einem hellen Raum mit Pflanzen"></div>
  <div class="abs hero-title">Familienberatung Stadlau</div>
  <div class="abs sq light" style="left:380px;top:465px;width:60px;height:70px"></div>
  <div class="abs sq" style="left:451px;top:465px;width:62px;height:70px"></div>

  <div class="abs service-img" style="left:35px;top:597px" role="img" aria-label="Foto: Einzelberatung im Beratungsraum"></div>
  <div class="abs service-text" style="left:236px;top:600px">
    <h2>Einzelberatung</h2>
    <p>Für den ganz persönlichen Weg zur Selbstbestimmung. Ist er einmal betreten, wird die persönliche Entwicklung ein wundervolles Abenteuer.</p>
  </div>

  <div class="abs service-img" style="left:466px;top:597px" role="img" aria-label="Foto: Paar im Beratungsgespräch"></div>
  <div class="abs service-text" style="left:663px;top:600px;width:196px">
    <h2>Paarberatung</h2>
    <p>Muster können aufgelöst werden! Gerne unterstütze ich Sie auf Ihrem Weg, sich in Ihrer Partnerschaft wieder auf deren Grundlage zu besinnen. Darauf aufzubauen, einen viel versprechenden Neubeginn zu wagen.</p>
  </div>

  <div class="abs service-img" style="left:35px;top:772px" role="img" aria-label="Foto: Eltern mit Kindern im Alltag"></div>
  <div class="abs service-text" style="left:236px;top:771px">
    <h2>Erziehungsberatung</h2>
    <p>Meine Aufgabe besteht darin, Sie in einem vertrauensvollen Rahmen zu unterstützen, eine neue Form der elterlichen Kooperation zu finden und Ihren Blick und Ihre Aufmerksamkeit auf die Bedürfnisse und Nöte der Kinder/des Kindes zu richten</p>
  </div>

  <div class="abs service-img" style="left:466px;top:772px" role="img" aria-label="Foto: Mutter liest mit Kindern ein Buch"></div>
  <div class="abs service-text" style="left:665px;top:771px;width:198px">
    <h2>Familie &amp; Kinder</h2>
    <p>Das Ziel einer Familientherapie ist, eine positive Beziehungs&shy;veränderung zwischen den einzelnen Familien&shy;mitgliedern zu erreichen. Respekt, gegenseitiges Verständ&shy;nis und Einfühlungs&shy;vermögen füreinander sind wesentlich für ein funktionierendes Zusammenleben in einer Familie.</p>
  </div>

  <section class="abs voices">
    <h2>Stimmen von Klienten</h2>
    <div class="abs quote" style="left:48px;width:378px">
      <p>Helga Brandtner zeichnet sich durch Wärme, Souveränität, Ruhe und Sorgfältigkeit aus. Sicher und liebevoll begleitet sie durch den Prozess. Sie ist neutral, aber interessiert. Man fühlt sich gut aufgehoben, auch wenn es "ans Eingemachte" geht.</p>
      <span class="who">Frau R. Klientin</span>
    </div>
    <span class="qmark" style="left:24px;top:48px">“</span>
    <span class="qmark" style="left:398px;top:150px">”</span>

    <div class="abs quote" style="left:475px;width:369px;padding-top:24px">
      <p>Mein Weg war voller Steine und Holz. Ich nahm den Besen in die Hand und kehrte. Frau Brandtner begleitete mich dabei.</p>
      <span class="who">Frau H. Klientin</span>
    </div>
    <span class="qmark" style="left:462px;top:48px">“</span>
    <span class="qmark" style="left:818px;top:150px">”</span>
  </section>

  <footer class="abs footer">Lindenweg 12/3, 1220 Vienna | familienberatung@helga-brandtner.at | Telephone: +43 660 481 27 19</footer>
</body>
</html>
```